School Rules Posters

I would like a design for four different posters. Each one has a different purpose:

1: The Three Main rules

2: The Rewards

3: The Consequences

4: Consequences

At the moment they are very boring and dry and I would like an icon for each rule with the text underneath?

I'd like the logo on it.

It is for a middle school so it cannot be 'too young'.

I don't mind if the posters are Portrait or Landscape. The posters need to provide pupils with clarity and cannot be too busy. They'll be made into A1.
I have attached an example from another school which has logos - I don't want the same thing but give's you an idea of icons.

```html
<!DOCTYPE html>
<html lang="en">
<head>
<meta charset="utf-8">
<title>The Hartwell Way – Rules</title>
<link rel="stylesheet" href="https://fonts.googleapis.com/css2?family=Barlow+Condensed:wght@400;500;700&display=swap">
<style>
  :root {
    --page-bg: #e6e6e6;
    --header-bg: #f9f9f9;
    --plum: #7b1a66;
    --band: #420c36;
    --band-divider: #2c0624;
    --cell-light: #721a5e;
    --cell-dark: #5f0a4b;
    --ink: #262626;
    --white: #ffffff;
  }
  * { box-sizing: border-box; margin: 0; padding: 0; }
  html, body {
    width: 1200px; height: 1000px; overflow: hidden;
    background: var(--page-bg);
    font-family: "Barlow Condensed", "Arial Narrow", sans-serif;
  }
  .poster {
    position: absolute; left: 97px; top: 144px;
    width: 1006px; height: 712px;
    background: var(--header-bg);
  }
  .poster-header { position: absolute; left: 0; top: 0; width: 100%; height: 205px; }
  .title {
    position: absolute; left: 304px; top: 58px;
    font-size: 61px; font-weight: 700; line-height: 1;
    color: var(--plum); letter-spacing: 0.5px; white-space: nowrap;
  }
  .subtitle {
    position: absolute; left: 304px; top: 125px;
    font-size: 47px; font-weight: 500; line-height: 1;
    color: var(--ink); letter-spacing: 0.4px; white-space: nowrap;
  }
  .values-band {
    position: absolute; left: 0; top: 205px; width: 100%; height: 102px;
    background: var(--band);
  }
  .value {
    position: absolute; top: 0; height: 102px;
    display: flex; align-items: center; justify-content: center;
    color: var(--white); font-size: 44px; font-weight: 700; letter-spacing: 0.4px;
  }
  .value--ready { left: 270px; width: 206px; }
  .value--respectful { left: 478px; width: 324px; }
  .value--safe { left: 804px; width: 202px; }
  .value-divider {
    position: absolute; top: 16px; width: 3px; height: 70px;
    background: var(--band-divider);
  }
  .crest-pennant { position: absolute; left: 21px; top: 0; width: 254px; height: 292px; }
  .school-name {
    position: absolute; left: 21px; top: 96px; width: 254px;
    text-align: center; color: var(--plum);
    font-size: 30px; font-weight: 700; line-height: 1.05; letter-spacing: 0.6px;
  }
  .rules-grid {
    position: absolute; left: 0; top: 307px; width: 100%; height: 405px;
    display: grid; grid-template-columns: repeat(5, 1fr); grid-template-rows: repeat(3, 1fr);
  }
  .rule {
    display: flex; flex-direction: column; align-items: center;
    padding-top: 22px; color: var(--white); text-align: center;
  }
  .rule--light { background: var(--cell-light); }
  .rule--dark { background: var(--cell-dark); }
  .rule-icon { width: 50px; height: 50px; fill: var(--white); }
  .rule-text {
    margin-top: 16px; font-size: 17.5px; font-weight: 400; line-height: 20px;
  }
</style>
</head>
<body>
<main class="poster">
  <header class="poster-header">
    <h1 class="title">THE HARTWELL WAY – RULES</h1>
    <p class="subtitle">HELPING US BE THE BEST WE CAN BE</p>
  </header>

  <section class="values-band">
    <div class="value value--ready">BE READY</div>
    <span class="value-divider" style="left:476px"></span>
    <div class="value value--respectful">BE RESPECTFUL</div>
    <span class="value-divider" style="left:802px"></span>
    <div class="value value--safe">BE SAFE</div>
  </section>

  <svg class="crest-pennant" viewBox="0 0 254 292">
    <path d="M3 0 V210 Q3 228 26 240 L127 288 L228 240 Q251 228 251 210 V0" fill="#ffffff" stroke="#420c36" stroke-width="5"/>
    <rect x="111" y="44" width="32" height="32" fill="#7b1a66"/>
  </svg>
  <div class="school-name">HARTWELL<br>ASHBY</div>

  <section class="rules-grid">
    <div class="rule rule--light">
      <svg class="rule-icon" viewBox="0 0 50 50"><circle cx="25" cy="11" r="8"/><path d="M9 30 Q9 22 17 21 H33 Q41 22 41 30 V46 H9Z"/><rect x="5" y="27" width="40" height="7" rx="3" fill="#721a5e"/><rect x="7" y="28" width="36" height="5" rx="2.5"/></svg>
      <p class="rule-text">Be Well<br>Presented</p>
    </div>
    <div class="rule rule--dark">
      <svg class="rule-icon" viewBox="0 0 50 50"><circle cx="25" cy="17" r="9"/><circle cx="19" cy="14" r="6"/><circle cx="31" cy="14" r="6"/><path d="M4 32 L24 36 V46 L4 42Z M46 32 L26 36 V46 L46 42Z"/><path d="M25 2 V5 M12 6 L14 8 M38 6 L36 8" stroke="#fff" stroke-width="2"/></svg>
      <p class="rule-text">Ready to learn<br>new ideas</p>
    </div>
    <div class="rule rule--light">
      <svg class="rule-icon" viewBox="0 0 50 50"><circle cx="20" cy="22" r="16" fill="none" stroke="#fff" stroke-width="3"/><path d="M20 12 V22 H28" stroke="#fff" stroke-width="3" fill="none"/><circle cx="38" cy="30" r="6"/><path d="M28 48 Q28 38 38 38 Q48 38 48 48Z"/></svg>
      <p class="rule-text">Punctual to meet<br>and great</p>
    </div>
    <div class="rule rule--dark">
      <svg class="rule-icon" viewBox="0 0 50 50"><ellipse cx="18" cy="32" rx="14" ry="8" fill="none" stroke="#fff" stroke-width="3"/><path d="M4 32 V37 Q18 48 32 37 V32" fill="none" stroke="#fff" stroke-width="3"/><path d="M30 20 L44 6 M34 6 H44 V16" stroke="#fff" stroke-width="3" fill="none"/></svg>
      <p class="rule-text">Have the right<br>equipment</p>
    </div>
    <div class="rule rule--light">
      <svg class="rule-icon" viewBox="0 0 50 50"><rect x="16" y="4" width="18" height="22" rx="4"/><rect x="12" y="27" width="26" height="5" rx="2"/><rect x="8" y="20" width="4" height="12" rx="2"/><rect x="38" y="20" width="4" height="12" rx="2"/><rect x="23" y="32" width="4" height="9"/><path d="M12 44 L25 40 L38 44" stroke="#fff" stroke-width="3" fill="none"/></svg>
      <p class="rule-text">Know<br>your seat</p>
    </div>

    <div class="rule rule--dark">
      <svg class="rule-icon" viewBox="0 0 50 50"><rect x="14" y="8" width="5" height="22" rx="2.5"/><rect x="20" y="4" width="5" height="24" rx="2.5"/><rect x="26" y="6" width="5" height="22" rx="2.5"/><rect x="32" y="10" width="5" height="20" rx="2.5"/><path d="M14 26 H37 V34 Q37 46 26 46 Q16 46 12 36 L7 26 Q9 22 13 26Z"/></svg>
      <p class="rule-text">Raise your<br>hand to talk</p>
    </div>
    <div class="rule rule--light">
      <svg class="rule-icon" viewBox="0 0 50 50"><circle cx="18" cy="12" r="8"/><path d="M4 42 Q4 24 18 24 Q28 24 30 32 V42Z"/><path d="M30 38 L35 32 L39 42 L43 34 L48 38" stroke="#fff" stroke-width="3" fill="none"/></svg>
      <p class="rule-text">Manners give<br>a great impressions</p>
    </div>
    <div class="rule rule--dark">
      <svg class="rule-icon" viewBox="0 0 50 50"><rect x="6" y="4" width="34" height="34" fill="none" stroke="#fff" stroke-width="3"/><path d="M14 46 V22 Q14 18 17 18 Q20 18 20 22 V16 Q20 12 23 12 Q26 12 26 16 V20 Q29 18 32 21 V34 Q32 46 22 46Z"/><path d="M42 2 L44 8 L50 10 L44 12 L42 18 L40 12 L34 10 L40 8Z"/></svg>
      <p class="rule-text">Leave your desk tidy<br>for the next class</p>
    </div>
    <div class="rule rule--light">
      <svg class="rule-icon" viewBox="0 0 50 50"><path d="M25 44 L7 26 Q1 18 7 10 Q15 3 25 13 Q35 3 43 10 Q49 18 43 26Z"/><path d="M12 30 L22 22 L28 28 M20 36 L30 28" stroke="#721a5e" stroke-width="3" fill="none"/></svg>
      <p class="rule-text">Respect every persons<br>right to learn and work</p>
    </div>
    <div class="rule rule--dark">
      <svg class="rule-icon" viewBox="0 0 50 50"><rect x="4" y="22" width="9" height="22"/><path d="M15 22 H22 L26 10 Q30 10 30 16 V22 H40 Q44 22 43 27 L40 42 Q39 44 36 44 H15Z"/><rect x="32" y="2" width="3" height="18"/><rect x="35" y="2" width="12" height="9"/></svg>
      <p class="rule-text">Show the best<br>version of you</p>
    </div>

    <div class="rule rule--light">
      <svg class="rule-icon" viewBox="0 0 50 50"><rect x="10" y="8" width="30" height="4"/><rect x="21" y="4" width="8" height="4"/><path d="M12 15 H38 L35 46 H15Z"/><path d="M20 20 V40 M25 20 V40 M30 20 V40" stroke="#721a5e" stroke-width="2.5"/></svg>
      <p class="rule-text">Throw litter in<br>the bin</p>
    </div>
    <div class="rule rule--dark">
      <svg class="rule-icon" viewBox="0 0 50 50"><circle cx="16" cy="9" r="5"/><path d="M10 16 H20 L24 30 H12 V44 H8 V22Z"/><rect x="26" y="24" width="22" height="4"/><rect x="35" y="28" width="4" height="16"/><rect x="28" y="18" width="6" height="6"/><path d="M4 20 V44" stroke="#fff" stroke-width="3"/></svg>
      <p class="rule-text">Eat and drink in the<br>designated areas</p>
    </div>
    <div class="rule rule--light">
      <svg class="rule-icon" viewBox="0 0 50 50"><circle cx="27" cy="7" r="5"/><path d="M22 14 H30 L32 28 L38 46 H33 L27 32 L22 46 H17 L22 28 L20 22 L16 28 L13 26Z"/></svg>
      <p class="rule-text">Walk quietly around the<br>school building and grounds</p>
    </div>
    <div class="rule rule--dark">
      <svg class="rule-icon" viewBox="0 0 50 50"><path d="M6 20 L25 6 L44 20 V46 H6Z"/><g fill="#5f0a4b"><rect x="11" y="22" width="6" height="6"/><rect x="22" y="22" width="6" height="6"/><rect x="33" y="22" width="6" height="6"/><rect x="11" y="32" width="6" height="6"/><rect x="33" y="32" width="6" height="6"/><rect x="21" y="34" width="8" height="12"/></g></svg>
      <p class="rule-text">Look after our<br>building and grounds</p>
    </div>
    <div class="rule rule--light">
      <svg class="rule-icon" viewBox="0 0 50 50"><rect x="30" y="4" width="8" height="42" rx="3"/><rect x="36" y="14" width="14" height="4" rx="2"/><path d="M2 20 H14 L26 24 Q30 26 28 30 H18 V34 H2Z"/></svg>
      <p class="rule-text">Hold doors open<br>for others</p>
    </div>
  </section>
</main>
</body>
</html>
```